Business Card Design

Harbor Refuse 284 is a waste collection business contracted to remove waste from city streets, parks and caravan parks.

Target Market(s)

CEO and Managing Directors

Industry/Entity Type

Business

Contact Information for Business Card

Harbor Refuse 284
Manager
Glen Parkes
0438261954
harborrefuse284@mailbox-example.com.au

Colors
33a6d7
ecf7fb

Requirements
Must have
• Must have eye catching design that stands out above others ( tender process can be very competitive ).
Nice to have
• A garbage truck on or in the logo somehow

```html
<!DOCTYPE html>
<html lang="en">
<head>
<meta charset="utf-8">
<title>Harbor Refuse 284 – Business Card</title>
<link rel="stylesheet" href="https://fonts.googleapis.com/css2?family=Open+Sans:wght@400;600;700&display=swap">
<style>
  :root {
    --backdrop: #2a2a2c;
    --card: #e4e5e7;
    --band: #0b0b0b;
    --brand-blue: #33a6d7;
    --ink: #141414;
    --white: #ffffff;
    --truck-light: #ecf7fb;
    --truck-mid: #c9cdd1;
  }
  * { box-sizing: border-box; margin: 0; padding: 0; }
  html, body {
    width: 1200px;
    height: 735px;
    overflow: hidden;
    background: var(--backdrop);
    font-family: "Open Sans", Arial, sans-serif;
  }
  .canvas {
    position: relative;
    width: 1200px;
    height: 735px;
  }
  .business-card {
    position: absolute;
    left: 160px;
    top: 98px;
    width: 880px;
    height: 540px;
    background: var(--card);
    border-radius: 40px;
    overflow: hidden;
  }
  .brand {
    position: absolute;
    left: 90px;
    top: 118px;
    display: flex;
    align-items: center;
    gap: 36px;
  }
  .brand-name {
    color: var(--brand-blue);
    font-weight: 700;
    font-size: 50px;
    line-height: 1;
    letter-spacing: -0.5px;
    white-space: nowrap;
  }
  .truck-illustration {
    width: 190px;
    height: 104px;
    background: linear-gradient(180deg, var(--white) 0%, var(--truck-light) 50%, var(--truck-mid) 100%);
  }
  .contact-band {
    position: absolute;
    left: 0;
    top: 312px;
    width: 100%;
    height: 112px;
    background: var(--band);
    color: var(--white);
  }
  .person {
    position: absolute;
    left: 100px;
    top: 24px;
  }
  .person-name {
    font-size: 32px;
    font-weight: 400;
    letter-spacing: 0.5px;
    text-transform: uppercase;
    line-height: 1.1;
  }
  .person-role {
    font-size: 20px;
    font-weight: 400;
    letter-spacing: 0.5px;
    text-transform: uppercase;
    margin-top: 4px;
    margin-left: 12px;
  }
  .phone {
    position: absolute;
    left: 440px;
    top: 26px;
    font-size: 30px;
    white-space: nowrap;
  }
  .phone-label {
    font-weight: 400;
    letter-spacing: 1px;
    margin-right: 12px;
  }
  .phone-number {
    font-weight: 700;
    letter-spacing: 0.5px;
  }
</style>
</head>
<body>
  <main class="canvas">
    <section class="business-card">
      <div class="brand">
        <span class="brand-name">Harbor Refuse 284</span>
        <div class="truck-illustration" role="img" aria-label="Illustration of a garbage truck"></div>
      </div>
      <div class="contact-band">
        <div class="person">
          <p class="person-name">Glen Parkes</p>
          <p class="person-role">Manager</p>
        </div>
        <p class="phone"><span class="phone-label">CALL:</span><span class="phone-number">0438261954</span></p>
      </div>
    </section>
  </main>
</body>
</html>
```